Website

I have a client that we built a website for about 10 years ago - https://www.pinloopcards.com.au/

We would like a fresh new design for it that looks more modern. All the elements, info that's on there needs to be the same but the whole design/layout needs to be modernised.

```html
<!DOCTYPE html>
<html lang="en">
<head>
<meta charset="utf-8">
<title>Pinloop Cards – Name Badges</title>
<link rel="stylesheet" href="https://fonts.googleapis.com/css2?family=Outfit:wght@400;500;600&family=Poppins:wght@400;500;600&display=swap">
<style>
:root{
  --red:#d3121b;
  --red-dark:#a90c14;
  --black:#0d0d0d;
  --ink:#1a1a1a;
  --muted:#6b6b6b;
  --grey-bg:#efeeee;
  --line:#d9d9d9;
  --white:#ffffff;
}
*{margin:0;padding:0;box-sizing:border-box}
html,body{width:1200px;height:4666px;overflow:hidden;background:var(--white)}
body{position:relative;font-family:"Poppins",sans-serif;color:var(--ink)}
.abs{position:absolute}
.head-red{font-family:"Outfit",sans-serif;font-weight:500;color:var(--red);font-size:27px;text-transform:uppercase;letter-spacing:-.3px;text-align:center;width:1200px;left:0}
.head-black{font-family:"Outfit",sans-serif;font-weight:500;color:var(--black);font-size:33px;text-transform:uppercase;letter-spacing:-.6px;text-align:center;width:1200px;left:0}
.btn{position:absolute;display:flex;align-items:center;justify-content:center;border-radius:40px;font-size:14px;font-weight:500;text-transform:uppercase;letter-spacing:.3px}
.btn-red{background:var(--red);color:var(--white)}
.btn-outline{border:1.5px solid var(--red);color:var(--red);background:var(--white)}
.btn-black{background:var(--black);color:var(--white)}
.btn-white{background:var(--white);color:var(--red)}
.brand{font-family:"Poppins",sans-serif;font-weight:600;color:var(--red);display:flex;align-items:center;gap:8px}
.brand .dot{width:14px;height:14px;border-radius:50%;background:var(--red)}

/* top bar */
.topbar{left:431px;top:0;width:655px;height:36px;background:var(--black);display:flex;font-size:12px;color:var(--white)}
.topbar .call{flex:0 0 317px;display:flex;align-items:center;justify-content:center;gap:8px}
.topbar .call span{color:var(--red)}
.topbar .links{flex:1;background:var(--red-dark);display:flex;align-items:center;justify-content:center;gap:14px}
.nav{top:70px;left:0;width:1200px;font-size:13px;text-transform:uppercase;color:var(--ink)}
.nav a{position:absolute;text-decoration:none;color:inherit}
.nav a.active{color:var(--red)}

/* hero */
.hero{left:0;top:0;width:1200px;height:560px;overflow:hidden}
.hero-photo{position:absolute;inset:0;background:linear-gradient(90deg,#dfe6ee 0%,#eef1f4 30%,#f4f4f4 55%,#e9eaec 80%,#d9dadd 100%)}
.hero-copy{position:absolute;left:0;width:1200px;text-align:center}
.hero-text{position:absolute;left:360px;top:238px;width:480px;text-align:center;font-size:15px;line-height:34px;color:var(--ink)}
.dots{position:absolute;display:flex;gap:14px}
.dots i{width:9px;height:9px;border-radius:50%;border:1.5px solid var(--red);display:block}
.dots i.on{background:var(--red)}

/* products */
.card{position:absolute;top:776px;width:235px;height:410px;background:var(--white);border-radius:10px;box-shadow:0 4px 16px rgba(0,0,0,.1);border-bottom:4px solid var(--red);overflow:hidden;text-align:center}
.card.dark{background:var(--black);color:var(--white)}
.card .photo{height:167px;width:100%}
.card .icon{position:absolute;left:81px;top:131px;width:72px;height:72px;border-radius:50%;background:var(--white);box-shadow:0 3px 10px rgba(0,0,0,.15);display:flex;align-items:center;justify-content:center}
.card h3{position:absolute;top:222px;width:100%;font-size:14px;font-weight:500;text-transform:uppercase}
.card p{position:absolute;top:258px;left:18px;right:18px;font-size:13.5px;line-height:30px;color:var(--muted)}
.card.dark p{color:var(--white)}
.card .more{position:absolute;top:360px;width:100%;font-size:13.5px;color:var(--red);text-transform:uppercase;font-weight:500}

/* about */
.about{left:0;top:1361px;width:1200px;height:516px;background:var(--grey-bg)}
.about-photo{position:absolute;left:112px;top:87px;width:438px;height:355px;background:linear-gradient(135deg,#5a5a5a,#b7b7b7 45%,#3d3d3d);border-radius:0 0 10px 10px}
.about-body{position:absolute;left:619px;font-size:15px;line-height:30px;color:var(--ink);width:472px}

/* why */
.why-title{font-size:14px;font-weight:500;text-transform:uppercase}
.why-text{font-size:14px;line-height:30px;color:var(--muted)}
.why-circle{position:absolute;width:88px;height:88px;border-radius:50%;background:var(--red);display:flex;align-items:center;justify-content:center}
.why-circle.black{background:var(--black)}

/* testimonials */
.trust{left:0;top:2873px;width:1200px;height:470px;background:var(--grey-bg)}
.quote{position:absolute;top:184px;width:433px;height:226px;background:var(--white);border:1px solid var(--line);border-radius:10px;text-align:center}
.quote .mark{position:absolute;top:-8px;left:40px;font-family:"Outfit",sans-serif;font-size:64px;font-weight:600;color:var(--red);line-height:1}
.quote h4{position:absolute;top:34px;width:100%;font-size:14px;font-weight:500}
.quote p{position:absolute;top:68px;left:30px;right:30px;font-size:14px;line-height:30px;color:var(--muted)}
.quote .who{position:absolute;top:176px;width:100%;font-size:13.5px;color:var(--red);text-transform:uppercase}
.arrow{position:absolute;width:32px;height:32px;border-radius:50%;display:flex;align-items:center;justify-content:center}

/* clients */
.client{position:absolute;top:3568px;font-size:17px;font-weight:600;color:#7a7a7a;text-align:center;width:125px}

/* cta & footer */
.cta-bg{left:0;top:3770px;width:1200px;height:896px;background:linear-gradient(180deg,#c8101a 0%,#e01b23 40%,#c0121a 100%)}
.cta-text{left:160px;width:880px;top:3888px;text-align:center;color:var(--white);font-size:15px;line-height:34px}
.foot-head{font-family:"Outfit",sans-serif;font-size:21px;font-weight:500;color:var(--red);text-transform:uppercase}
.foot-links{font-size:13px;color:var(--white);text-transform:uppercase;line-height:38px}
.foot-contact{left:757px;font-size:13px;color:var(--white)}
.foot-icon{position:absolute;left:757px;width:42px;height:42px;border-radius:50%;background:var(--red);display:flex;align-items:center;justify-content:center}
.foot-line{left:108px;top:4597px;width:984px;height:1px;background:#2f2f2f}
.copyright{left:0;top:4620px;width:1200px;text-align:center;font-size:12.5px;color:var(--white)}
</style>
</head>
<body>

<!-- Hero -->
<section class="abs hero">
  <div class="hero-photo" role="img" aria-label="Photo of a smiling receptionist and a smiling barista each wearing a name badge, with a blurred reception sign behind"></div>
  <svg class="abs" style="left:0;top:0" width="1200" height="560" viewBox="0 0 1200 560">
    <path d="M0 482 C320 560 820 585 1200 425 L1200 560 L0 560 Z" fill="#fff"/>
    <path d="M22 487 C330 540 760 565 1200 392 L1200 428 C820 585 330 560 22 487 Z" fill="#d3121b"/>
  </svg>
  <div class="hero-copy head-red" style="top:130px">Do your people</div>
  <div class="hero-copy head-black" style="top:172px">Need name badges fast?</div>
  <p class="hero-text">At Pinloop Cards we focus on providing our clients badges and name tags at lightning speed and to the highest quality. With no minimum order, free setup and SUPER FAST delivery you've come the right place!</p>
  <div class="btn btn-red" style="left:514px;top:410px;width:158px;height:42px">Get started</div>
  <div class="dots" style="left:562px;top:510px"><i class="on"></i><i></i><i></i><i></i></div>
</section>

<!-- Header -->
<div class="abs brand" style="left:114px;top:26px;font-size:22px"><span class="dot"></span>Pinloop Cards</div>
<div class="abs topbar">
  <div class="call"><svg width="12" height="12" viewBox="0 0 24 24"><path d="M6.6 10.8a15 15 0 0 0 6.6 6.6l2.2-2.2a1 1 0 0 1 1-.25 11 11 0 0 0 3.6.6 1 1 0 0 1 1 1V20a1 1 0 0 1-1 1A17 17 0 0 1 3 4a1 1 0 0 1 1-1h3.5a1 1 0 0 1 1 1 11 11 0 0 0 .6 3.6 1 1 0 0 1-.25 1Z" fill="#d3121b"/></svg><span>CALL US:</span> 1300 555 214</div>
  <div class="links">ARTWORK REQUIREMENTS <span>|</span> CONTACT US</div>
</div>
<nav class="abs nav">
  <a class="active" style="left:429px">Home</a>
  <a style="left:503px">Our products</a>
  <a style="left:646px">Price list</a>
  <a style="left:751px">Re-sellers trade info</a>
  <a style="left:957px">Info</a>
  <a style="left:1022px">Payment</a>
</nav>
<svg class="abs" style="left:420px;top:60px" width="60" height="12" viewBox="0 0 60 12"><path d="M2 10 Q30 -2 58 6" stroke="#d3121b" stroke-width="2.5" fill="none"/></svg>

<!-- Products -->
<h2 class="abs head-red" style="top:645px">High-quality name</h2>
<h2 class="abs head-black" style="top:690px">Badges designed for business</h2>

<div class="card" style="left:107px">
  <div class="photo" role="img" aria-label="Photo of a full colour name badge on a lanyard" style="background:linear-gradient(135deg,#e6e6e6,#bfbfbf)"></div>
  <div class="icon"><svg width="36" height="36" viewBox="0 0 36 36" fill="none" stroke="#d3121b" stroke-width="2"><rect x="4" y="8" width="28" height="20" rx="2"/><circle cx="12" cy="17" r="3"/><path d="M7 24c1-3 9-3 10 0M20 14h8M20 19h8M20 24h5"/></svg></div>
  <h3>Full colour name badges</h3>
  <p>For the most professional name badge for your company or event,</p>
  <div class="more">Read more &nbsp;›</div>
</div>
<div class="card dark" style="left:357px">
  <div class="photo" role="img" aria-label="Photo of round button badges pinned to a denim jacket" style="background:linear-gradient(135deg,#3a3328,#8a6a3a 60%,#2a2a2a)"></div>
  <div class="icon"><svg width="36" height="36" viewBox="0 0 36 36" fill="none" stroke="#d3121b" stroke-width="2"><circle cx="18" cy="18" r="12"/><circle cx="18" cy="18" r="6"/><path d="M10 30h16"/></svg></div>
  <h3>Button badges</h3>
  <p>Custom button badges are the perfect promotional tools for product launches,</p>
  <div class="more">Read more &nbsp;›</div>
</div>
<div class="card" style="left:608px">
  <div class="photo" role="img" aria-label="Photo of a reusable black name tag with lanyard beside a compass" style="background:linear-gradient(135deg,#6b4a2a,#3a2a1c 60%,#8a6b3c)"></div>
  <div class="icon"><svg width="36" height="36" viewBox="0 0 36 36" fill="none" stroke="#d3121b" stroke-width="2"><rect x="9" y="6" width="18" height="25" rx="2"/><path d="M15 6v-2h6v2"/><circle cx="18" cy="15" r="3"/><path d="M13 23c1-3 9-3 10 0M13 27h10"/></svg></div>
  <h3>Reusable name badges</h3>
  <p>If you're looking for name tags that you can use several times in different</p>
  <div class="more">Read more &nbsp;›</div>
</div>
<div class="card" style="left:858px">
  <div class="photo" role="img" aria-label="Photo of an engraved metal name tag on a chain" style="background:linear-gradient(135deg,#efe9e2,#cfc3b5)"></div>
  <div class="icon"><svg width="36" height="36" viewBox="0 0 36 36" fill="none" stroke="#d3121b" stroke-width="2"><path d="M8 6h20l-10 14Z"/><path d="M18 20v10M12 30h12M13 12h10"/></svg></div>
  <h3>Engraved name badges</h3>
  <p>If your company prefers to use the traditional engraving on your name</p>
  <div class="more">Read more &nbsp;›</div>
</div>
<div class="btn btn-red" style="left:427px;top:1237px;width:176px;height:40px">More products</div>
<div class="btn btn-outline" style="left:621px;top:1237px;width:152px;height:40px">View details</div>

<!-- About -->
<section class="abs about">
  <svg class="abs" style="left:80px;top:45px" width="480" height="120" viewBox="0 0 480 120"><path d="M2 75 C60 10 300 -10 475 40 L470 52 C300 10 90 40 30 110 Z" fill="#d3121b"/></svg>
  <div class="about-photo" role="img" aria-label="Photo of a group of colleagues clapping and celebrating"></div>
  <h2 class="abs" style="left:619px;top:58px;font-family:'Outfit',sans-serif;font-weight:500;font-size:27px;color:var(--red);text-transform:uppercase;letter-spacing:-.3px">Reliable name badge</h2>
  <h2 class="abs" style="left:619px;top:102px;font-family:'Outfit',sans-serif;font-weight:500;font-size:33px;color:var(--black);text-transform:uppercase;letter-spacing:-.6px">Solutions across Australia</h2>
  <p class="about-body" style="top:170px">When it comes to name badges, tags, and other ID products, there's no service more trusted in Australia than Pinloop Cards.</p>
  <p class="about-body" style="top:277px;text-align:justify">True to our name, our name badges Australia company specialises in producing a wide range of high-quality identity tags and products.</p>
  <div class="btn btn-red" style="left:620px;top:404px;width:142px;height:40px">Read more</div>
</section>

<!-- Why us -->
<h2 class="abs head-red" style="top:1952px">Why businesses</h2>
<h2 class="abs head-black" style="top:1998px">Across Australia choose us</h2>
<svg class="abs" style="left:0;top:2080px" width="1200" height="560" viewBox="0 2080 1200 560">
  <g stroke="#d3121b" stroke-width="1.3" stroke-dasharray="4 4" fill="none">
    <path d="M365 2170 L470 2220"/><path d="M835 2170 L730 2220"/>
    <path d="M365 2410 L460 2370"/><path d="M835 2410 L740 2370"/>
    <path d="M600 2495 L600 2560"/>
  </g>
  <circle cx="600" cy="2295" r="200" fill="#e6e6e6"/>
  <circle cx="600" cy="2295" r="158" fill="#0d0d0d"/>
  <text x="600" y="2304" text-anchor="middle" font-family="Poppins, sans-serif" font-weight="600" font-size="28" fill="#ffffff">Pinloop Cards</text>
</svg>

<div class="why-circle" style="left:273px;top:2095px"><svg width="44" height="44" viewBox="0 0 44 44" fill="none" stroke="#fff" stroke-width="2"><path d="M10 14l14-6 12 6v16l-12 6-14-6Z"/><path d="M10 14l14 6 12-6M24 20v16"/><path d="M2 22h6M4 28h6"/></svg></div>
<div class="abs" style="left:100px;top:2208px;width:260px;text-align:right"><div class="why-title">Super-fast delivery</div><p class="why-text" style="margin-top:10px">We know timing matters. That's why our streamlined production process and efficient dispatch.</p></div>

<div class="why-circle" style="left:836px;top:2095px"><svg width="44" height="44" viewBox="0 0 44 44" fill="none" stroke="#fff" stroke-width="2"><circle cx="22" cy="22" r="12"/><circle cx="22" cy="22" r="5"/><path d="M22 4v6M22 34v6M4 22h6M34 22h6M9 9l4 4M31 31l4 4M9 35l4-4M31 13l4-4"/></svg></div>
<div class="abs" style="left:836px;top:2208px;width:260px"><div class="why-title">In-depth customisation</div><p class="why-text" style="margin-top:10px">Every name badge is fully customisable to reflect your brand, your team, and your workplace.</p></div>

<div class="why-circle" style="left:273px;top:2398px"><svg width="44" height="44" viewBox="0 0 44 44" fill="none" stroke="#fff" stroke-width="2"><path d="M22 6l16 16-16 16L6 22Z"/><path d="M14 14l16 16M30 14L14 30M22 6v32M6 22h32"/></svg></div>
<div class="abs" style="left:100px;top:2510px;width:260px;text-align:right"><div class="why-title">Free design setup</div><p class="why-text" style="margin-top:10px">Simply provide your details and logo, and our team will prepare a clean, professional layout that's ready for production.</p></div>

<div class="why-circle black" style="left:836px;top:2398px"><svg width="44" height="44" viewBox="0 0 44 44" fill="none" stroke="#fff" stroke-width="2"><rect x="8" y="12" width="22" height="22"/><path d="M12 30l18-18 4 4-18 18-6 2Z"/><path d="M34 6v6M31 9h6"/></svg></div>
<div class="abs" style="left:836px;top:2510px;width:260px"><div class="why-title" style="color:var(--red)">High-quality materials</div><p class="why-text" style="margin-top:10px">We use only carefully selected materials to ensure every name badge looks professional and stands up to daily wear.</p></div>

<div class="why-circle" style="left:556px;top:2564px"><svg width="44" height="44" viewBox="0 0 44 44" fill="none" stroke="#fff" stroke-width="2"><rect x="8" y="8" width="28" height="28"/><rect x="14" y="14" width="16" height="16"/><path d="M4 8h4M36 8h4M4 36h4M36 36h4M14 26l5-5 4 4 4-3 3 4"/></svg></div>
<div class="abs" style="left:440px;top:2678px;width:320px;text-align:center"><div class="why-title">Free postage</div><p class="why-text" style="margin-top:10px">Enjoy free postage on all orders, with no hidden costs or surprises at checkout.</p></div>

<!-- Testimonials -->
<section class="abs trust">
  <h2 class="abs head-red" style="top:46px">Trusted by</h2>
  <h2 class="abs head-black" style="top:92px">Businesses across Australia</h2>
  <div class="quote" style="left:152px">
    <div class="mark">“</div>
    <h4>HI PRIYA</h4>
    <p>Thank you and your staff for the professional grace with which you rectified this problem. We really appreciate it...</p>
    <div class="who">Renee &amp; Lara - Graceful Moves</div>
  </div>
  <div class="quote" style="left:614px">
    <div class="mark">“</div>
    <h4>HI PRIYA AND TEAM</h4>
    <p>Badges arrived yesterday and we are absolutely thrilled with them. Many thanks for your attention to detail, courtesy in your emails...</p>
    <div class="who">Dorothy - Garden City Bonnet Club</div>
  </div>
  <div class="arrow" style="left:51px;top:280px;background:var(--black)"><svg width="14" height="14" viewBox="0 0 14 14"><path d="M9 2L4 7l5 5" stroke="#fff" stroke-width="2.2" fill="none"/></svg></div>
  <div class="arrow" style="left:1104px;top:280px;background:var(--red)"><svg width="14" height="14" viewBox="0 0 14 14"><path d="M5 2l5 5-5 5" stroke="#fff" stroke-width="2.2" fill="none"/></svg></div>
</section>

<!-- Clients -->
<h2 class="abs head-red" style="top:3420px">Our list of</h2>
<h2 class="abs head-black" style="top:3466px">Valued clients</h2>
<div class="client" style="left:110px">Corvalink</div>
<div class="client" style="left:253px">Harbourhope</div>
<div class="client" style="left:392px">Baywater Primary</div>
<div class="client" style="left:530px">Lantern Hotels</div>
<div class="client" style="left:657px">Northfuel</div>
<div class="client" style="left:796px">Coastline Club</div>
<div class="client" style="left:935px">Stride Employment</div>
<div class="dots" style="left:563px;top:3678px"><i class="on"></i><i></i><i></i></div>

<!-- CTA + footer -->
<div class="abs cta-bg" role="img" aria-label="Red tinted photo of a team at work"></div>
<h2 class="abs head-black" style="top:3834px;color:var(--white);font-size:28px">Ready to create your name badges?</h2>
<p class="abs cta-text">Design professional name badges that reflect your brand and arrive fast. Whether you need a single badge or a bulk order for your entire team, we make the process simple from start to finish.</p>
<div class="btn btn-black" style="left:389px;top:3991px;width:201px;height:40px">Design your badge</div>
<div class="btn btn-white" style="left:610px;top:3991px;width:199px;height:40px">Get a bulk quote</div>

<svg class="abs" style="left:0;top:4100px" width="1200" height="566" viewBox="0 0 1200 566"><path d="M0 160 C260 150 520 10 1200 5 L1200 566 L0 566 Z" fill="#0d0d0d"/></svg>

<div class="abs brand" style="left:0;top:4184px;width:1200px;justify-content:center;font-size:22px;color:var(--red)"><span class="dot"></span>Pinloop Cards</div>

<div class="abs foot-head" style="left:130px;top:4250px">Quick links</div>
<div class="abs foot-links" style="left:130px;top:4298px">Home<br>Products<br>Price list<br>Re-sellers / trade info<br>FAQs<br>Artwork requirements<br>Contact us</div>
<div class="abs foot-links" style="left:413px;top:4298px">Payment<br>Nurse name badges<br>Identification name badges<br>Magnetic name tags<br>Plastic name badges<br>Site map</div>

<div class="abs foot-head" style="left:757px;top:4250px">Contact us</div>
<div class="foot-icon" style="top:4310px"><svg width="18" height="18" viewBox="0 0 24 24"><path d="M6.6 10.8a15 15 0 0 0 6.6 6.6l2.2-2.2a1 1 0 0 1 1-.25 11 11 0 0 0 3.6.6 1 1 0 0 1 1 1V20a1 1 0 0 1-1 1A17 17 0 0 1 3 4a1 1 0 0 1 1-1h3.5a1 1 0 0 1 1 1 11 11 0 0 0 .6 3.6 1 1 0 0 1-.25 1Z" fill="#fff"/></svg></div>
<div class="abs foot-contact" style="left:822px;top:4321px">1300 555 214</div>
<div class="foot-icon" style="top:4388px"><svg width="18" height="18" viewBox="0 0 24 24" fill="none" stroke="#fff" stroke-width="2"><rect x="4" y="9" width="16" height="10" rx="1"/><path d="M7 9V4h10v5M8 14h8"/></svg></div>
<div class="abs foot-contact" style="left:822px;top:4399px">03 9000 4172</div>
<div class="foot-icon" style="top:4466px"><svg width="18" height="18" viewBox="0 0 24 24"><path d="M12 2a7 7 0 0 0-7 7c0 5 7 13 7 13s7-8 7-13a7 7 0 0 0-7-7Zm0 9.5A2.5 2.5 0 1 1 12 6.5a2.5 2.5 0 0 1 0 5Z" fill="#fff"/></svg></div>
<div class="abs foot-contact" style="left:822px;top:4462px;line-height:30px">PO BOX 4021, RIDGEWOOD VALE<br>QLD 4350</div>

<div class="abs foot-line"></div>
<div class="abs copyright">© COPYRIGHT 2026. PINLOOP CARDS. ALL RIGHTS RESERVED.</div>

</body>
</html>
```